Refresh Home Page for Photography Training Site

http://brannowlessons.example/

My site is looking kind of out-of-date, so it's time for a face lift. I want to bring it up to date with a more modern web look.

What I need from you is a home page design concept. No coding, just a PSD design, but it MUST be something that a coder could build into an efficient, fast-loading page. After the home page design contest is finished, we can work together privately, if you want to continue, to design the rest of the pages in the site for additional fees.

Functionally, the new page needs to do the same job as the current home page, just do it more efficiently (if possible) while looking fresh and modern.

Sites I like
http://quelt.example/ (clean, modern)

Competitor sites:
http://varnocourses.example/
http://www.ivanmorrowimaging.example/

Target Market(s)

Amateur and semi-professional photographers

Industry/Entity Type

Training

Requirements
Must have
• MUST HAVE
1. A prominent space where testimonials appear in rotation, one after another (instead of the one large testimonial on the current site).

2. My photo in the header. It can be smaller than at present. If you prefer you can use the black and white photo from the about page. Put a signature saying Dan Brannow near the photo, in a better handwritten style than the current signature, which is a lame font.

3. Tagline "Learn Photography and Image Editing the Easy Way"
Should not have
• No flash or other fancy technology. (However it is acceptable to design an area that would be an image carousel, where one image changes to another, then another, etc. Like the Ivan Morrow or Quelt site. That is not too fancy, but it's optional).

```html
<!DOCTYPE html>
<html lang="en">
<head>
<meta charset="utf-8">
<title>Brannow Training – Home</title>
<link rel="stylesheet" href="https://fonts.googleapis.com/css2?family=Arimo:wght@400;700&family=Open+Sans:wght@300;400&family=Tinos:ital@1&family=Mrs+Saint+Delafield&display=swap">
<style>
:root{
  --page-bg:#e9e9e9;
  --sheet-bg:#f3f3f3;
  --sheet-line:#c9c9c9;
  --panel-bg:#ffffff;
  --panel-line:#dedede;
  --text:#3c3c3c;
  --muted:#9a9a9a;
  --accent:#4f8db3;
  --accent-light:#8ccbe6;
  --ribbon:#6fb9de;
  --dark:#3e3e3e;
}
*{box-sizing:border-box;margin:0;padding:0}
html,body{width:891px;height:1200px;overflow:hidden}
body{background:var(--page-bg);font-family:"Arimo",Arial,sans-serif;color:var(--text);position:relative}
.sheet{position:absolute;left:13px;top:21px;width:866px;height:1157px;background:var(--sheet-bg);border:1px solid var(--sheet-line)}
.abs{position:absolute}

/* header */
.portrait{left:76px;top:32px;width:124px;height:124px;background:linear-gradient(180deg,#d9c3a8 0%,#c7a88a 45%,#5e93c9 80%,#4a86c4 100%);border-radius:50px 50px 0 0}
.signature{left:190px;top:88px;font-family:"Mrs Saint Delafield",cursive;font-size:38px;line-height:44px;color:#555}
.brand-name{left:357px;top:106px;font-family:"Open Sans",sans-serif;font-weight:400;font-size:17px;color:#4a4a4a;letter-spacing:.3px}
.brand-tagline{left:357px;top:129px;font-family:"Open Sans",sans-serif;font-size:8px;color:#777;letter-spacing:.1px}
.main-nav{left:338px;top:47px;height:37px;display:flex;background:#fff;border:1px solid #d3d3d3;box-shadow:0 1px 2px rgba(0,0,0,.08)}
.main-nav a{display:flex;align-items:center;justify-content:center;height:100%;font-size:11px;font-weight:700;color:#333;text-decoration:none;border-left:1px solid #dcdcdc}
.main-nav a:first-child{border-left:0}
.social{top:109px;width:26px;height:26px;border-radius:50%;background:#fff;border:1px solid #d5d5d5;box-shadow:0 1px 2px rgba(0,0,0,.1)}

/* slider */
.slider{left:76px;top:156px;width:740px;height:371px;background:#fff;border:1px solid #e1e1e1;box-shadow:0 12px 18px -10px rgba(0,0,0,.25)}
.slide{left:20px;top:19px;width:701px;height:334px;background:linear-gradient(90deg,#f2eff3 0%,#e8e2ea 60%,#e3dce6 100%);border:1px solid #ddd}
.slide-photo{left:400px;top:0;width:299px;height:332px;background:linear-gradient(135deg,#f0ebef 0%,#9a6a45 25%,#e2c2ac 50%,#f0dccd 75%,#c49775 100%)}
.slide-title{left:22px;top:66px;width:390px;font-size:22px;line-height:31px;color:#3a3a3a;font-weight:400}
.slide-copy{left:22px;top:138px;width:330px;font-size:12px;line-height:18px;color:#444}
.btn-pill{left:24px;top:232px;width:103px;height:30px;border-radius:15px;background:linear-gradient(#eef7fb,#cfe6f1);border:3px solid #a7d6ec;font-size:10.5px;color:#3f84aa;display:flex;align-items:center;justify-content:center}
.ribbon-wrap{overflow:hidden}
.ribbon{background:var(--ribbon);color:#fff;font-weight:700;text-align:center;transform:rotate(-45deg);box-shadow:0 2px 3px rgba(0,0,0,.2)}
.ribbon.hot{font-size:14px;color:#1f5f86;line-height:26px}
.ribbon.free{transform:rotate(45deg);font-size:13px;color:#1f5f86;line-height:22px}
.nav-arrow{top:316px;width:27px;height:50px;background:var(--dark)}
.nav-arrow.prev{left:49px;border-radius:25px 0 0 25px}
.nav-arrow.next{left:816px;border-radius:0 25px 25px 0}
.dot{top:560px;width:12px;height:12px;border-radius:50%;background:#9d9d9d;box-shadow:inset 0 1px 2px rgba(0,0,0,.3)}
.dot.active{background:var(--accent-light)}

/* panels */
.panel{background:var(--panel-bg);border:1px solid var(--panel-line);box-shadow:0 2px 4px rgba(0,0,0,.08)}
.panel-title{font-size:18px;color:var(--accent);font-weight:400}
.rule{height:1px;background:#e3e3e3}
.thumb{border:5px solid #d9d9d9;background:#888}
.item-title{font-size:12px;font-weight:700;color:var(--accent);line-height:15px}
.item-copy{font-size:10px;line-height:16px;color:#333}
.item-copy .new{color:#57a8d3;font-weight:700}
.meta{font-family:"Tinos",Georgia,serif;font-style:italic;font-size:9.5px;color:#9a9a9a}
.more{font-size:10.5px;font-weight:700;color:var(--accent);display:flex;align-items:center;gap:7px}
.see-all{font-size:10px;color:var(--accent);display:flex;align-items:center;gap:9px}
.quote{font-size:13px;line-height:18px;color:#5ea0c6}
.quote-by{font-size:9.5px;color:#aaa}
.quote-by b{color:#999}
.footer{top:1144px;right:66px;font-size:8px;color:#666}
</style>
</head>
<body>
<div class="sheet"></div>

<header>
  <div class="abs portrait" role="img" aria-label="Portrait photo of Dan Brannow"></div>
  <div class="abs signature">Dan Brannow</div>
  <div class="abs brand-name">BRANNOW TRAINING</div>
  <div class="abs brand-tagline">LEARNING PHOTOGRAPHY AND IMAGE EDITING THE EASY WAY</div>
  <nav class="abs main-nav">
    <a href="#" style="width:69px">Home</a>
    <a href="#" style="width:73px">About</a>
    <a href="#" style="width:84px">Courses</a>
    <a href="#" style="width:105px">Free Tutorials</a>
    <a href="#" style="width:60px">FAQs</a>
    <a href="#" style="width:83px">Contact</a>
  </nav>
  <span class="abs social" style="left:714px"></span>
  <span class="abs social" style="left:750px"></span>
  <span class="abs social" style="left:785px"></span>
</header>

<section class="abs slider">
  <div class="abs slide">
    <div class="abs slide-photo" role="img" aria-label="Portrait photograph of a woman with long hair"></div>
    <h1 class="abs slide-title">Start learning today how to take your own professional looking photographs</h1>
    <p class="abs slide-copy">From ameteur to professional theres a course, or tutorial to teach you different pro techniques for taking the perfect photo, step by step</p>
    <a class="abs btn-pill">Find out more</a>
  </div>
</section>
<div class="abs ribbon-wrap" style="left:72px;top:153px;width:120px;height:120px">
  <div class="abs ribbon hot" style="left:-38px;top:30px;width:170px">WHAT'S HOT!</div>
</div>
<div class="abs nav-arrow prev"><svg width="27" height="50"><path d="M17 19l-6 6 6 6" stroke="#fff" stroke-width="3" fill="none"/></svg></div>
<div class="abs nav-arrow next"><svg width="27" height="50"><path d="M10 19l6 6-6 6" stroke="#fff" stroke-width="3" fill="none"/></svg></div>
<span class="abs dot" style="left:402px"></span>
<span class="abs dot" style="left:421px"></span>
<span class="abs dot active" style="left:440px"></span>
<span class="abs dot" style="left:458px"></span>
<span class="abs dot" style="left:477px"></span>

<section class="abs panel" style="left:65px;top:599px;width:489px;height:503px">
  <h2 class="abs panel-title" style="left:15px;top:15px">Latest Online Training Courses</h2>
  <div class="abs rule" style="left:11px;top:45px;width:452px"></div>

  <div class="abs thumb" style="left:18px;top:65px;width:133px;height:98px;background:linear-gradient(90deg,#3b3b3b,#b98b6e 60%,#f0f0f0)" role="img" aria-label="Software box and portrait of a model"></div>
  <div class="abs item-title" style="left:173px;top:69px">Pixelforge basics for photographers</div>
  <p class="abs item-copy" style="left:173px;top:89px;width:270px"><span class="new">NEW!</span> Learn the core Pixelforge skills every photographer needs in this easy, 10-lesson video course.</p>
  <div class="abs meta" style="left:173px;top:160px">9 (series) videos &nbsp;|&nbsp; 3 hours</div>
  <div class="abs more" style="left:372px;top:157px"><svg width="9" height="12"><path d="M2 1l5 5-5 5" stroke="#5b7d92" stroke-width="3" fill="none"/></svg>Find out more</div>
  <div class="abs rule" style="left:11px;top:182px;width:452px"></div>

  <div class="abs thumb" style="left:18px;top:195px;width:133px;height:99px;background:linear-gradient(90deg,#6b4e3a,#3d6a4a 45%,#aa8060 75%,#d8c7b8)" role="img" aria-label="Collage of headshot photos with a small flash"></div>
  <div class="abs item-title" style="left:173px;top:199px;width:250px">How to shoot professional headshots on a budget with a small flash</div>
  <p class="abs item-copy" style="left:173px;top:233px;width:275px">This 9-video course, will teach you all you need to know about off-camera lighting with your digital SLR's detachable flash!</p>
  <div class="abs meta" style="left:173px;top:294px">13 (series) videos &nbsp;|&nbsp; 2.5 hours</div>
  <div class="abs more" style="left:372px;top:291px"><svg width="9" height="12"><path d="M2 1l5 5-5 5" stroke="#5b7d92" stroke-width="3" fill="none"/></svg>Find out more</div>
  <div class="abs rule" style="left:11px;top:316px;width:452px"></div>

  <div class="abs thumb" style="left:18px;top:329px;width:133px;height:99px;background:linear-gradient(135deg,#f5f5f5,#2a2a2a 45%,#555 70%,#eee)" role="img" aria-label="Software box and a digital camera"></div>
  <div class="abs item-title" style="left:173px;top:333px">Darkbench basics for photographers</div>
  <p class="abs item-copy" style="left:173px;top:353px;width:275px">Learn how Darkbench can help you take your photography to the next level in this introductory video course.</p>
  <div class="abs meta" style="left:173px;top:428px">1 videos &nbsp;|&nbsp; - hours</div>
  <div class="abs more" style="left:372px;top:425px"><svg width="9" height="12"><path d="M2 1l5 5-5 5" stroke="#5b7d92" stroke-width="3" fill="none"/></svg>Find out more</div>
  <div class="abs rule" style="left:11px;top:452px;width:452px"></div>

  <div class="abs see-all" style="left:18px;top:471px"><svg width="22" height="22"><circle cx="11" cy="11" r="10" fill="#6fb9de" stroke="#bfe1f1" stroke-width="2"/><path d="M9 6l5 5-5 5" stroke="#fff" stroke-width="2.5" fill="none"/></svg>See all courses available</div>
</section>

<section class="abs panel" style="left:572px;top:599px;width:259px;height:326px">
  <h2 class="abs panel-title" style="left:18px;top:15px">Online Tutorials</h2>
  <div class="abs thumb" style="left:19px;top:52px;width:82px;height:61px;border-width:3px;background:linear-gradient(90deg,#2e1d10,#c58a4a 50%,#3a2614)" role="img" aria-label="Chess pieces with shallow depth of field"></div>
  <div class="abs item-title" style="left:112px;top:54px;width:120px">Understanding Depth of field</div>
  <div class="abs more" style="left:112px;top:94px"><svg width="9" height="12"><path d="M2 1l5 5-5 5" stroke="#5b7d92" stroke-width="3" fill="none"/></svg>Find out more</div>
  <div class="abs rule" style="left:19px;top:124px;width:220px"></div>
  <div class="abs thumb" style="left:19px;top:135px;width:82px;height:61px;border-width:3px;background:linear-gradient(90deg,#5d4630,#c79a72 50%,#6b7a3e)" role="img" aria-label="Video still of a model photo shoot"></div>
  <div class="abs item-title" style="left:112px;top:137px;width:120px">Model Shot at Granite Beat Hotel</div>
  <div class="abs more" style="left:112px;top:177px"><svg width="9" height="12"><path d="M2 1l5 5-5 5" stroke="#5b7d92" stroke-width="3" fill="none"/></svg>Find out more</div>
  <div class="abs rule" style="left:19px;top:207px;width:220px"></div>
  <div class="abs thumb" style="left:19px;top:218px;width:82px;height:61px;border-width:3px;background:linear-gradient(90deg,#1a1a1a,#5a5a5a 50%,#d8b9a4)" role="img" aria-label="Woman holding a camera with flash"></div>
  <div class="abs item-title" style="left:112px;top:220px;width:120px">Flash Photography tips (video)</div>
  <div class="abs more" style="left:112px;top:260px"><svg width="9" height="12"><path d="M2 1l5 5-5 5" stroke="#5b7d92" stroke-width="3" fill="none"/></svg>Find out more</div>
  <div class="abs see-all" style="left:19px;top:293px"><svg width="22" height="22"><circle cx="11" cy="11" r="10" fill="#6fb9de" stroke="#bfe1f1" stroke-width="2"/><path d="M9 6l5 5-5 5" stroke="#fff" stroke-width="2.5" fill="none"/></svg>See all free available tutorials</div>
</section>
<div class="abs ribbon-wrap" style="left:742px;top:592px;width:95px;height:95px">
  <div class="abs ribbon free" style="left:-5px;top:22px;width:130px">FREE!</div>
</div>

<section class="abs panel" style="left:572px;top:939px;width:259px;height:163px">
  <h2 class="abs panel-title" style="left:16px;top:14px">Testimonals</h2>
  <svg class="abs" style="left:18px;top:44px" width="14" height="10"><text x="0" y="14" font-family="Georgia,serif" font-size="22" font-weight="700" fill="#777">“</text></svg>
  <p class="abs quote" style="left:40px;top:43px;width:185px">I love your videos! I can learn more in one hour than in a month of studying photography books!</p>
  <div class="abs quote-by" style="left:40px;top:121px"><b>Marvin T</b> &nbsp;|&nbsp; Chicago IL</div>
  <svg class="abs" style="left:231px;top:117px" width="14" height="12"><text x="0" y="16" font-family="Georgia,serif" font-size="22" font-weight="700" fill="#777">”</text></svg>
</section>

<footer class="abs footer">Terms &amp; Conditions &nbsp;|&nbsp; Privacy &nbsp;&nbsp;&nbsp;&nbsp; © 2011 Dan Brannow</footer>
</body>
</html>
```